Business Telephone Service Brochure

I need a brochure designed to help sell our VoIP service. The brochure needs to be clean, attention getting, professional and have 3 key areas of information (Key Features, Benefits & Service Plans). Here is an idea of what we are looking for https://www.artflockly.com/design/52930487. Need to also include how much the customer could save. See this for an example https://42mockups.com/postcard-flyer-design/contests/voip-sales-flyer-template-replicate-attached-358209. The Service Plan section needs to allow room for two types of plans. One plan includes the phone and has a 12, 24 and 36 month option. Each term (12,24,36) will have its own monthly cost per device. The second service option is no-commitment monthly with a single per month price per device. The included features section should allow for up to 16 features to be listed. The benefits should allow for 4-6 benefits to be listed. Also include room for Logo, business address, website, phone number and email.

Target Market(s)

Small to medium business with 1-100 employees.

Industry/Entity Type

Telecommunications

Font styles to use
Serif

Colors

Designer to choose colors to be used in the design.

Requirements
Must have
• Key Feature, Benefits and Service Plans (i.e. Pricing). Company logo, phone, email and website. Must have "Save up to x%!" and catch attention.
Nice to have
• Limited colors. I am not setting a hard limit, please take the liberty to do what you feel is needed. Just keep in mind we want it to be clean, professional and attention getting without being to flashy or obnoxious.
Should not have
• Nothing busy or distracting.

```html
<!DOCTYPE html>
<html lang="en">
<head>
<meta charset="utf-8">
<title>Voxera – Telecommunications Service Provider</title>
<link rel="stylesheet" href="https://fonts.googleapis.com/css2?family=Open+Sans:wght@400;600;700;800&display=swap">
<style>
  :root {
    --navy: #1a2e9e;
    --navy-deep: #14237f;
    --orange: #f57c1f;
    --orange-deep: #d9560f;
    --orange-soft: #f59a52;
    --ice: #dcebf3;
    --ice-deep: #a9c6d8;
    --paper: #ffffff;
    --stage: #cfcfcf;
    --ink-light: #ffffff;
  }
  * { box-sizing: border-box; margin: 0; padding: 0; }
  html, body { width: 1200px; height: 1200px; overflow: hidden; }
  body { background: var(--stage); font-family: "Open Sans", Arial, sans-serif; }

  .flyer { position: absolute; left: 220px; top: 60px; width: 760px; height: 1080px; background: var(--paper); overflow: hidden; box-shadow: 0 10px 30px rgba(0,0,0,.18); }

  .hero-photo { position: absolute; left: 0; top: 0; width: 760px; height: 420px;
    background: radial-gradient(ellipse at 45% 55%, #ffffff 0%, var(--ice) 45%, var(--ice-deep) 100%); }
  .phone-photo { position: absolute; left: 520px; top: 60px; width: 200px; height: 180px; border-radius: 14px;
    background: linear-gradient(150deg, #5b6470, #2e343c); }
  .corner-frame { position: absolute; left: 560px; top: 22px; width: 170px; height: 120px;
    border-top: 4px solid var(--orange); border-right: 4px solid var(--orange); }

  .brand { position: absolute; left: 40px; top: 150px; }
  .brand-name { font-size: 64px; font-weight: 700; color: var(--navy); line-height: 1; letter-spacing: -2px; }
  .brand-tagline { font-size: 9px; color: #555; margin-top: 2px; letter-spacing: .3px; }
  .headline { position: absolute; left: 40px; top: 250px; }
  .headline-top { font-size: 24px; font-weight: 600; color: var(--navy); }
  .headline-bottom { font-size: 24px; font-weight: 600; color: var(--orange); }
  .divider { position: absolute; left: 330px; top: 246px; width: 3px; height: 62px; background: var(--orange); }
  .website { position: absolute; left: 350px; top: 266px; display: flex; align-items: center; gap: 8px;
    font-size: 14px; font-weight: 600; color: var(--navy); }

  .blue-field { position: absolute; left: 0; top: 0; }

  .section-tab { position: absolute; font-size: 20px; font-weight: 700; color: var(--navy); }
  .tab-benefits { left: 545px; top: 302px; }
  .tab-features { left: 105px; top: 402px; }
  .tab-service { left: 70px; top: 722px; }

  .point-list { position: absolute; list-style: none; color: var(--ink-light); font-size: 11.5px; font-weight: 600; }
  .point-list li { display: flex; align-items: center; gap: 10px; height: 18px; }
  .point-list li::before { content: ""; width: 12px; height: 12px; border-radius: 50%; border: 2px solid var(--orange);
    background: radial-gradient(circle, var(--orange) 0 2px, transparent 2.5px); flex: none; }
  .benefits-list { left: 440px; top: 350px; }
  .features-list { left: 40px; top: 446px; }

  .savings-callout { position: absolute; left: 470px; top: 585px; padding: 12px 26px; border-radius: 30px;
    background: var(--orange); color: var(--ink-light); font-size: 24px; font-weight: 800; letter-spacing: .3px; }

  .plans { position: absolute; left: 20px; top: 715px; width: 720px; height: 250px;
    background: linear-gradient(180deg, var(--orange) 0%, var(--orange-deep) 100%); }
  .plans-label { position: absolute; left: 0; top: 0; width: 250px; height: 48px; background: var(--paper);
    border-bottom-right-radius: 18px; }
  .term-col { position: absolute; top: 0; height: 180px; border-left: 1px solid rgba(255,255,255,.55);
    color: var(--ink-light); font-size: 13px; font-weight: 600; padding: 12px 0 0 12px; }
  .term-col .price { display: block; font-size: 11px; font-weight: 400; margin-top: 6px; }
  .col-monthly { left: 250px; width: 115px; background: rgba(255,255,255,.06); }
  .col-12 { left: 365px; width: 115px; background: rgba(255,255,255,.1); }
  .col-24 { left: 480px; width: 120px; background: rgba(255,255,255,.14); }
  .col-36 { left: 600px; width: 120px; background: var(--orange-soft); opacity: .95; }

  .plan-rows { position: absolute; left: 0; top: 60px; width: 720px; list-style: none; }
  .plan-rows li { height: 30px; border-top: 1px solid rgba(255,255,255,.55); color: var(--ink-light);
    font-size: 11px; padding: 8px 0 0 14px; }
  .plan-rows li:last-child { border-bottom: 1px solid rgba(255,255,255,.55); }

  .footnotes { position: absolute; left: 14px; top: 190px; list-style: none; color: var(--ink-light); font-size: 9.5px; }
  .footnotes li { display: flex; align-items: center; gap: 8px; height: 20px; }
  .footnotes li::before { content: ""; width: 9px; height: 9px; border-radius: 50%; border: 2px solid #fff; flex: none; }

  .contact-bar { position: absolute; left: 0; top: 985px; width: 760px; height: 95px; background: var(--navy);
    display: flex; align-items: center; justify-content: space-between; padding: 0 30px; color: var(--ink-light); font-size: 12.5px; }
  .contact-item { display: flex; align-items: center; gap: 10px; }
  .contact-icon { width: 24px; height: 24px; border-radius: 50%; background: #fff; display: flex; align-items: center; justify-content: center; }
</style>
</head>
<body>
<main class="flyer">
  <div class="hero-photo" role="img" aria-label="Light blue circuit-board background with a hand touching a glowing interface"></div>
  <div class="corner-frame"></div>
  <div class="phone-photo" role="img" aria-label="Grey desk IP phone with orange wireless signal arcs"></div>

  <svg class="blue-field" width="760" height="1080" viewBox="0 0 760 1080" aria-hidden="true">
    <path d="M0 420 H80 Q92 420 96 434 Q100 446 114 446 H256 Q270 446 274 434 Q278 420 290 420 H400 V320 H520 Q532 320 536 334 Q540 346 554 346 H650 Q664 346 668 334 Q672 320 684 320 H760 V700 H0 Z" fill="#1a2e9e"/>
    <path d="M0 560 L760 420 V700 H0 Z" fill="#14237f" opacity=".35"/>
  </svg>

  <div class="brand">
    <div class="brand-name">voxera</div>
    <div class="brand-tagline">Internet · Telephone · Security · Networking</div>
  </div>
  <div class="headline">
    <div class="headline-top">Telecommunications</div>
    <div class="headline-bottom">Service Provider</div>
  </div>
  <div class="divider"></div>
  <div class="website">
    <span>www.voxeratel.net</span>
    <svg width="22" height="22" viewBox="0 0 22 22" aria-hidden="true"><g fill="none" stroke="#1a2e9e" stroke-width="1.6"><circle cx="11" cy="11" r="9.5"/><ellipse cx="11" cy="11" rx="4.5" ry="9.5"/><path d="M1.5 11H20.5M3 6H19M3 16H19"/></g></svg>
  </div>

  <h2 class="section-tab tab-benefits">Benefits</h2>
  <ul class="point-list benefits-list">
    <li>No expensive onsite telephone equipment</li>
    <li>Easily scale up or down and needs change</li>
    <li>Free telephone/email support</li>
    <li>Lower monthly cost</li>
    <li>Increase reliability</li>
    <li>Easy self-administration</li>
  </ul>

  <div class="savings-callout">Save up to 40%!</div>

  <h2 class="section-tab tab-features">Key Features</h2>
  <ul class="point-list features-list">
    <li>Unlimited local and long distance calling</li>
    <li>HD Voice</li>
    <li>Business SMS/Text Messaging</li>
    <li>Personal and Shared Voicemail Boxes</li>
    <li>Audio Conferencing</li>
    <li>Intercom</li>
    <li>Mobile App</li>
    <li>Auto Attendant/Interactive Voice Routing</li>
    <li>Free web or email fax</li>
    <li>Web admin portal</li>
    <li>Music On Hold - Customizable</li>
    <li>Simultaneous ring / follow-me</li>
    <li>Redundancy/Failover – Never miss a call</li>
  </ul>

  <section class="plans">
    <div class="term-col col-monthly">Monthly<span class="price">$21.95</span></div>
    <div class="term-col col-12">12 month term<span class="price">$24.95</span></div>
    <div class="term-col col-24">24 month term<span class="price">$22.95</span></div>
    <div class="term-col col-36">36 month term<span class="price">$20.95</span></div>
    <div class="plans-label"></div>
    <ul class="plan-rows">
      <li>¹Phone service only (phone sold separately)</li>
      <li>Service + ²Orvia T20 Phone</li>
      <li>Service + ²Orvia T20 Phone</li>
      <li>Service + ²Orvia T20 Phone</li>
    </ul>
    <ul class="footnotes">
      <li>¹For monthly service you may purchase the Orvia T20 phone for $65 each, less taxes and shipping.</li>
      <li>²Orvia T20 phones are rented and due upon cancellation. Customer pays return shipping.</li>
    </ul>
  </section>
  <h2 class="section-tab tab-service">Service</h2>

  <footer class="contact-bar">
    <div class="contact-item">
      <span class="contact-icon"><svg width="12" height="14" viewBox="0 0 12 14" aria-hidden="true"><path d="M6 0a5 5 0 0 1 5 5c0 4-5 9-5 9S1 9 1 5a5 5 0 0 1 5-5z" fill="#1a2e9e"/><circle cx="6" cy="5" r="1.8" fill="#fff"/></svg></span>
      <span>2145 Linden Ave. Riverton, NY 10920</span>
    </div>
    <div class="contact-item">
      <span class="contact-icon"><svg width="14" height="14" viewBox="0 0 14 14" aria-hidden="true"><circle cx="7" cy="7" r="2.5" fill="none" stroke="#1a2e9e" stroke-width="1.6"/><path d="M9.5 7v1.2a1.8 1.8 0 0 0 3.5 0V7A6 6 0 1 0 10 12" fill="none" stroke="#1a2e9e" stroke-width="1.6"/></svg></span>
      <span>hello@voxeratel.net</span>
    </div>
    <div class="contact-item">
      <span class="contact-icon"><svg width="12" height="12" viewBox="0 0 12 12" aria-hidden="true"><path d="M2.5 0.5l2 2.5-1.2 1.5a7 7 0 0 0 4.2 4.2L9 7.5l2.5 2-1.5 2C5 11.5.5 7 .5 2z" fill="#1a2e9e"/></svg></span>
      <span>+1-202-555-0188</span>
    </div>
  </footer>
</main>
</body>
</html>
```